REDESIGN MAIN BANNER IMAGE FOR MARKETING WEBSITE

I feel like my main banner image is too busy but I like it but i want to see other options. www.brightlanepromoworks.biz I want a nice professional clean design that goes with current theme of site. Must look professional and show the variety of incentives we offer but not be overwelming.

My business is called Brightlane Promo Works and I provide businesses around the world with marketing incentives that they can use to create exciting promotions and contest and marketing giveaways to help attract more customers.

I provide a variety of different types of incentives such as Vacation Certificates, Dining Vouchers, Hotel Savings Cards, Smart Watches, Etc. that businesses can use in their marketing efforts.

I want my main banner image to reflect the variety of different categories of incentives... that I offer here: https://www.brightlanepromoworks.biz/incentives

We can use images of certificates or images.....I just want the content to be the same:

CONTENT FOR MAIN BANNER IMAGE:
INCREASE LEADS AND SALES OVERNIGHT

CREATE EXCITING MARKETING PROMOTIONS GIVING AWAY SMART DEVICES, VACATION CERTIFICATES, DINING VOUCHERS AND OTHER INCENTIVES TO YOUR CUSTOMERS

GET A FREE SAMPLE PACKAGE FOR A LIMITED TIME ONLY

Target Market(s)

b2b business owners, ceo, president, owner, founder

Industry/Entity Type

Promotional

Requirements
Must have
• Hi guys keep in mind the finished product will have to be 1800x840

Nice to have
• I want a nice professional clean design that goes with current theme of site. Must look professional and show the variety of incentives we offer but not be overwelming.
Should not have

```html
<!DOCTYPE html>
<html lang="en">
<head>
<meta charset="utf-8">
<title>Brightlane Promo Works – Main Banner</title>
<link rel="stylesheet" href="https://fonts.googleapis.com/css2?family=Poppins:wght@300;400;600&family=Unbounded:wght@800&display=swap">
<style>
  :root {
    --page: #ffffff;
    --blue-light: #1772b8;
    --blue-dark: #0a4e88;
    --green: #4caf50;
    --white: #ffffff;
    --frame: #8a98a8;
    --flyer-grey: #c9d3de;
    --flyer-red: #b3242b;
    --flyer-dark: #23232e;
    --flyer-sky: #7fa6cf;
    --flyer-night: #3a2a4a;
  }
  * { margin: 0; padding: 0; box-sizing: border-box; }
  html, body {
    width: 1200px; height: 666px; overflow: hidden;
    background: var(--page);
  }
  .canvas { position: relative; width: 1200px; height: 666px; }
  .banner {
    position: absolute; left: 182px; top: 141px;
    width: 757px; height: 354px;
    background: linear-gradient(90deg, var(--blue-light) 0%, var(--blue-light) 38%, var(--blue-dark) 100%);
    border: 1px solid var(--frame);
    overflow: hidden;
  }
  .banner__topbar {
    position: absolute; left: 0; top: 0; width: 100%; height: 7px;
    background: var(--green);
  }
  .banner__stripe { position: absolute; left: 0; top: 7px; }

  .incentive-stack { position: absolute; left: 0; top: 0; width: 300px; height: 354px; }
  .flyer {
    position: absolute;
    box-shadow: 0 5px 12px rgba(0,0,0,0.35);
  }
  .flyer--watch {
    left: 54px; top: 56px; width: 136px; height: 196px;
    transform: rotate(-6deg);
    background: linear-gradient(180deg, var(--flyer-grey) 0%, var(--white) 40%, var(--flyer-grey) 100%);
  }
  .flyer--hotel {
    left: 40px; top: 104px; width: 120px; height: 176px;
    transform: rotate(-14deg);
    background: linear-gradient(180deg, var(--white) 0%, var(--flyer-sky) 35%, var(--white) 60%, var(--flyer-red) 100%);
  }
  .flyer--dining {
    left: 150px; top: 104px; width: 110px; height: 178px;
    transform: rotate(9deg);
    background: linear-gradient(180deg, var(--white) 0%, var(--flyer-night) 30%, var(--flyer-dark) 100%);
  }
  .flyer--vacation {
    left: 80px; top: 78px; width: 136px; height: 200px;
    transform: rotate(1.5deg);
    background: linear-gradient(180deg, var(--flyer-dark) 0%, var(--flyer-night) 22%, var(--white) 36%, var(--flyer-red) 48%, var(--white) 56%, var(--white) 100%);
  }

  .brand {
    position: absolute; left: 300px; top: 51px;
    display: flex; align-items: center; gap: 12px;
  }
  .brand__mark {
    width: 44px; height: 37px;
    border: 2px solid var(--white);
  }
  .brand__name {
    font-family: "Poppins", sans-serif; font-weight: 600;
    font-size: 19px; color: var(--white); letter-spacing: 0.3px;
  }
  .headline {
    position: absolute; left: 300px; top: 111px;
    font-family: "Unbounded", sans-serif; font-weight: 800;
    font-size: 25px; line-height: 29px; color: var(--white);
    text-transform: uppercase; letter-spacing: 0.8px;
    text-shadow: 1px 2px 3px rgba(0,0,0,0.35);
    white-space: nowrap;
  }
  .lead {
    position: absolute; left: 299px; top: 173px; width: 420px;
    font-family: "Poppins", sans-serif; font-weight: 300;
    font-size: 14.4px; line-height: 20px; color: var(--white);
    white-space: nowrap;
  }
  .cta {
    position: absolute; left: 299px; top: 258px;
    width: 190px; height: 46px;
    text-align: center; color: var(--white);
    text-decoration: none;
  }
  .cta__shape { position: absolute; left: 0; top: 0; filter: drop-shadow(0 3px 3px rgba(0,0,0,0.3)); }
  .cta__label {
    position: relative; display: block; padding-top: 5px;
    font-family: "Unbounded", sans-serif; font-weight: 800;
    font-size: 10.5px; line-height: 12px; letter-spacing: 0.4px;
  }
  .cta__note {
    position: relative; display: block; margin-top: 2px;
    font-family: "Poppins", sans-serif; font-weight: 400; font-size: 7px;
  }
</style>
</head>
<body>
<div class="canvas">
  <section class="banner">
    <div class="banner__topbar"></div>
    <svg class="banner__stripe" width="757" height="347" viewBox="0 0 757 347" aria-hidden="true">
      <polygon points="193,0 231,0 9,347 0,347 0,335" fill="var(--white)"/>
    </svg>

    <div class="incentive-stack">
      <div class="flyer flyer--watch" role="img" aria-label="Smartwatch giveaway certificate"></div>
      <div class="flyer flyer--hotel" role="img" aria-label="Hotel stay savings certificate"></div>
      <div class="flyer flyer--dining" role="img" aria-label="Dining voucher certificate"></div>
      <div class="flyer flyer--vacation" role="img" aria-label="Las Vegas vacation certificate with city night photos"></div>
    </div>

    <div class="brand">
      <span class="brand__mark"></span>
      <span class="brand__name">Brightlane Promo Works</span>
    </div>

    <h1 class="headline">Increase leads<br>and sales overnight</h1>

    <p class="lead">Create exciting marketing promotions giving away<br>Smart devices, vacation certificates, dining vouchers<br>and other incentives to your customers.</p>

    <a class="cta" href="https://www.brightlanepromoworks.biz/incentives">
      <svg class="cta__shape" width="190" height="46" viewBox="0 0 190 46" aria-hidden="true">
        <polygon points="0,0 190,0 186,39 95,45 4,39" fill="var(--green)"/>
      </svg>
      <span class="cta__label">GET A FREE<br>SAMPLE PACKAGE</span>
      <span class="cta__note">for a limited time only!</span>
    </a>
  </section>
</div>
</body>
</html>
```